Bref créative
Brochures for sophisticated nutrition products
Velvet Crest Products
The brochures to be designed should come across richly textured, for someone who likes elite, high quality, luxury products. We will be printing the brochures using foil inks and foil stamped ink, to bring out the colors. There are 6 brochures needed (6 different products). The brochure should bring out the vivid colors of the products themselves as well. When someone holds these brochures in their hands the though that should come to mind is "This must be expensive, high quality products" Please reference files of what the products look like.
Salon & Spa
The target audience is anyone looking to be fit, healthy, happy.
I am open to new ideas on the layouts of brochures, I would consider tri-fold, double folded. 8.5 x 14 should be the size of the brochures.
This is the current layout and feel of the website. You can see the colors of the products here. To get the details of what the content should be, please visit www.qlorbamerica.example and go to the products section. The content there is what we need to use for the brochures.
file 2
file 3
file 4
file 5
Company Logo File
Label for Product called: SOLO chocolate. The bottle color to go on the brochure is black, like the KVR product bottles.
Label for Product called: SOLO vanilla. The bottle color to go on the brochure is black, like the KVR product bottles.
Product called: HoTaru. Additional to this Box are the individual packets that go into it, which will be uploaded in another file.
Product called: HoTaru (Packets).
Image for Product called: KVR.
Image for product called: Flare
Image for product called: PQL
Supplement Facts Content for all products and Brochures
KVR Brochure Content
Flare Brochure Content
SOLO Brochure Content
HoTaru Brochure Content
PQL Brochure Content

```html
<!DOCTYPE html>
<html lang="en">
<head>
<meta charset="utf-8">
<title>Flare Brochure – Velvet Crest Products</title>
<link rel="stylesheet" href="https://fonts.googleapis.com/css2?family=Oswald:wght@500;700&family=Open+Sans:wght@400;600;700&family=Great+Vibes&display=swap">
<style>
  :root {
    --bg: #d9d4cc;
    --brown: #4a2613;
    --brown-dark: #351a0c;
    --green: #6b9a1e;
    --green-light: #86b52c;
    --cream: #f6efe2;
    --red: #8c1c12;
    --white: #ffffff;
    --ink: #2b2b2b;
  }
  * { box-sizing: border-box; margin: 0; padding: 0; }
  html, body { width: 1200px; height: 901px; overflow: hidden; }
  body {
    background: var(--bg);
    font-family: "Open Sans", Arial, sans-serif;
    position: relative;
  }
  .brochure {
    position: absolute;
    left: 22px; top: 100px;
    width: 1156px; height: 700px;
    display: flex;
    box-shadow: 0 14px 30px rgba(0,0,0,.25);
  }
  .panel { width: 385.33px; height: 100%; position: relative; padding: 34px 30px; }
  .panel--info, .panel--facts { background: var(--brown); color: var(--cream); }
  .panel--facts { border-left: 1px solid var(--brown-dark); border-right: 1px solid var(--brown-dark); }
  .panel--cover { background: var(--white); color: var(--ink); text-align: center; }

  .info-title { font-family: "Oswald", sans-serif; font-weight: 500; font-size: 22px; color: var(--green-light); margin-bottom: 16px; }
  .info-text { font-size: 13px; line-height: 1.65; margin-bottom: 14px; }
  .info-images { position: absolute; left: 30px; right: 30px; bottom: 34px; display: flex; gap: 12px; }
  .info-images div { flex: 1; height: 110px; border-radius: 4px; }
  .img-berry { background: radial-gradient(circle at 40% 40%, #a34a3a, #5b1a14); }
  .img-citrus { background: radial-gradient(circle at 50% 45%, #f0b45a, #c97526); }

  .box { background: var(--green); border-radius: 14px; padding: 20px 22px; color: var(--white); }
  .box + .box { margin-top: 22px; }
  .box-title { font-family: "Oswald", sans-serif; font-weight: 700; font-size: 26px; margin-bottom: 10px; }
  .facts-row { display: flex; justify-content: space-between; font-size: 12.5px; padding: 5px 0; border-bottom: 1px solid rgba(255,255,255,.45); }
  .facts-row--head { font-weight: 700; border-bottom: 3px solid var(--white); }
  .facts-note { font-size: 11px; margin-top: 8px; }
  .no-text { font-size: 12.5px; line-height: 1.6; margin-bottom: 8px; }

  .brand { display: flex; align-items: center; justify-content: center; gap: 8px; font-weight: 700; font-size: 15px; color: var(--brown); margin-top: 4px; }
  .brand-dot { width: 12px; height: 12px; border-radius: 50%; background: var(--brown); }
  .headline { font-family: "Oswald", sans-serif; font-weight: 700; font-size: 46px; line-height: 1.05; color: var(--red); margin-top: 26px; letter-spacing: 1px; }
  .tagline { font-family: "Great Vibes", cursive; font-size: 40px; color: var(--green); margin-top: 2px; }
  .product-visual {
    margin: 20px auto 0; width: 300px; height: 330px; border-radius: 8px;
    background: radial-gradient(ellipse at 55% 50%, #b8321c 0%, #7a1a10 38%, #efe9df 70%, #ffffff 100%);
  }
  .web { position: absolute; left: 0; right: 0; bottom: 34px; font-size: 14px; font-weight: 600; color: var(--ink); }
</style>
</head>
<body>
  <main class="brochure">
    <section class="panel panel--info">
      <h2 class="info-title">Why Choose Flare</h2>
      <p class="info-text">A daily blend of natural fruit and plant extracts crafted to support a balanced metabolism and steady energy throughout your day.</p>
      <p class="info-text">Take two capsules each morning with water before a meal. Pair with regular exercise and a sensible diet for best results.</p>
      <p class="info-text">Each capsule is made in a certified facility and tested for purity and quality.</p>
      <div class="info-images">
        <div class="img-berry" role="img" aria-label="Photo of dark red fruit"></div>
        <div class="img-citrus" role="img" aria-label="Photo of golden fruit slices"></div>
      </div>
    </section>

    <section class="panel panel--facts">
      <div class="box box--facts">
        <h2 class="box-title">Supplement Facts</h2>
        <div class="facts-row"><span>Serving Size 2 Capsules</span></div>
        <div class="facts-row"><span>Servings Per Container 30</span></div>
        <div class="facts-row facts-row--head"><span>Amount Per Serving</span><span>% Daily Value</span></div>
        <div class="facts-row"><span>Green Coffee Extract</span><span>400 mg</span></div>
        <div class="facts-row"><span>Mangosteen Extract</span><span>200 mg</span></div>
        <div class="facts-row"><span>Black Pepper Extract</span><span>10 mg</span></div>
        <div class="facts-row"><span>Green Tea Leaf</span><span>150 mg</span></div>
        <div class="facts-row"><span>Chromium</span><span>200 mcg</span></div>
        <p class="facts-note">Daily Value not established.</p>
      </div>
      <div class="box box--free">
        <h2 class="box-title">NO</h2>
        <p class="no-text">Gluten, Dairy, Soy, Sugar, Fish, Preservatives, Artificial Colors or Flavors.</p>
        <p class="no-text">Vegetarian Capsules. Store in a cool, dry place.</p>
        <p class="no-text">These statements have not been evaluated by the FDA. This product is not intended to diagnose, treat, cure or prevent any disease.</p>
      </div>
    </section>

    <section class="panel panel--cover">
      <div class="brand"><span class="brand-dot"></span>Velvet Crest Products</div>
      <h1 class="headline">FLARE FAT<br>TONE UP</h1>
      <p class="tagline">Feel Great</p>
      <div class="product-visual" role="img" aria-label="Flare supplement bottle with mangosteen fruit, green leaves and black peppercorns"></div>
      <p class="web">www.qlorbamerica.example</p>
    </section>
  </main>
</body>
</html>
```